Easy Business Card / Presentation Cover Design Project

We are looking for a business card design, covers for powerpoint presentations for investors, and possibly simple stationary for a Chicago real estate development firm. Our new logo is attached below.

We rehab and provide newly constructed homes. We are not a real estate brokerage firm (i.e., agents such as Meridale 47) and only operate in the Chicago area.

In terms of design, sophisticated and high end that would appeal to investors (theme should resemble investment banks, hedge funds, private equity rather than tech startup).

Target Market(s)

Investors, banks, financing sources

Industry/Entity Type

Real Estate

Requirements
Must have
• Two deliverables here. 1) Business card 2) Covers for powerpoint presentation.

Must be able to look sophisticated and high end when printed. Please think through the type of printing that will be needed. Would prefer something that can be printed in raised ink but digital is ok as well.

Will be printed on heavy paper.

Business Card: Horizontal Layout, no black backgrounds,

For presentation front cover, should include logo only. For back cover, should include contact info. Horizontal and should not contain any information that will need to be changed (i.e. date or client name)
Nice to have
• Would like to have the edges colored but not required. Please show multiple designs
Should not have
• Should not have any die cut or embossed type of designs. Shape should be standard size.

We are not a design firm, a retail firm, or a consumer product firm.

Please do not incorporate a house, buildings, etc. This must be very professional looking.

```html
<!DOCTYPE html>
<html lang="en">
<head>
<meta charset="utf-8">
<title>Harlow Crest – Stationery and Presentation Cover</title>
<link href="https://fonts.googleapis.com/css2?family=Lora:wght@400;600&display=swap" rel="stylesheet">
<style>
  :root {
    --brand-blue: #4a9bef;
    --brand-grey: #4d5459;
    --paper: #f3f3f2;
    --white: #ffffff;
    --backdrop: #d8d8d8;
    --ink: #3a3f44;
  }
  * { box-sizing: border-box; margin: 0; padding: 0; }
  html, body { width: 1200px; height: 1013px; overflow: hidden; }
  body {
    background: var(--backdrop);
    font-family: "Lora", Georgia, serif;
    color: var(--ink);
    position: relative;
  }
  .section-label {
    position: absolute;
    font-size: 11px;
    color: #222;
  }
  .piece { position: absolute; overflow: hidden; }
  .ring { position: absolute; border-radius: 50%; }

  /* wordmark */
  .wordmark { display: flex; align-items: center; gap: 8px; }
  .wordmark .dot { border-radius: 50%; background: var(--brand-blue); flex: none; }
  .wordmark .name { color: var(--brand-grey); font-weight: 600; white-space: nowrap; letter-spacing: .02em; }

  /* envelope */
  .envelope { left: 224px; top: 66px; width: 362px; height: 183px; background: var(--brand-blue); }
  .envelope .window { position: absolute; left: 31px; top: 88px; width: 154px; height: 65px; background: var(--paper); border-radius: 3px; }
  .envelope .ring { left: 277px; top: 95px; width: 90px; height: 90px; border: 3px solid var(--white); }

  /* business cards */
  .card { top: 272px; width: 150px; height: 83px; box-shadow: 0 1px 2px rgba(0,0,0,.15); }
  .card-back { left: 267px; background: var(--brand-blue); }
  .card-back .ring { left: 38px; top: 5px; width: 72px; height: 72px; border: 3px solid var(--white); }
  .card-front { left: 438px; background: var(--paper); padding: 8px 10px; }
  .card-front .name { font-size: 9px; }
  .card-front .dot { width: 12px; height: 12px; }
  .card-front .wordmark { gap: 4px; }
  .card-front .holder { margin-top: 8px; font-size: 4.5px; color: var(--brand-blue); letter-spacing: .04em; }
  .card-front .details { margin-top: 3px; font-size: 4px; line-height: 1.4; color: var(--brand-blue); }
  .card-front .ring { left: 112px; top: 40px; width: 44px; height: 44px; border: 2px solid var(--brand-blue); }

  /* letterhead */
  .letterhead { left: 642px; top: 62px; width: 348px; height: 490px; background: var(--paper); box-shadow: 0 2px 6px rgba(0,0,0,.18); }
  .letterhead .wordmark { position: absolute; left: 38px; top: 42px; }
  .letterhead .dot { width: 30px; height: 30px; }
  .letterhead .name { font-size: 15px; }
  .letterhead .contact { position: absolute; left: 221px; top: 36px; font-size: 4.6px; line-height: 1.55; color: var(--brand-blue); }
  .letterhead .contact h4 { font-weight: 400; font-size: 6.5px; letter-spacing: .05em; margin-bottom: 3px; }
  .letterhead .contact .web { margin-top: 4px; }
  .letter { position: absolute; left: 38px; top: 120px; width: 272px; font-size: 5.6px; line-height: 1.55; color: var(--ink); }
  .letter .meta { font-weight: 600; margin-bottom: 13px; }
  .letter p { margin-bottom: 9px; text-align: justify; }
  .letter .sign { margin-top: 12px; }
  .letterhead .ring { left: 218px; top: 369px; width: 120px; height: 120px; border: 4px solid var(--brand-blue); }

  /* presentation covers */
  .cover { top: 617px; width: 491px; height: 346px; }
  .cover-front { left: 97px; background: var(--paper); }
  .cover-front .edge { position: absolute; right: 0; top: 0; width: 16px; height: 100%; background: var(--brand-blue); }
  .cover-front .wordmark { position: absolute; left: 50px; top: 132px; gap: 16px; }
  .cover-front .dot { width: 80px; height: 80px; }
  .cover-front .name { font-size: 38px; font-weight: 400; }
  .cover-back { left: 602px; background: var(--brand-blue); color: var(--white); }
  .cover-back .ring { left: 313px; top: 0; width: 182px; height: 182px; margin-top: -40px; border: 5px solid var(--white); }
  .cover-back .contact { position: absolute; left: 32px; top: 197px; font-size: 16px; line-height: 1.2; }
  .cover-back .contact .phones { margin-top: 21px; }
  .cover-back .contact .web { margin-top: 21px; }
</style>
</head>
<body>

  <div class="section-label" style="left:97px; top:50px;">Stationery Mock-Up</div>

  <div class="piece envelope">
    <div class="window"></div>
    <div class="ring"></div>
  </div>

  <div class="piece card card-back"><div class="ring"></div></div>

  <div class="piece card card-front">
    <div class="wordmark"><span class="dot"></span><span class="name">Harlow Crest</span></div>
    <div class="holder">YOUR NAME GO HERE</div>
    <div class="details">
      Str. Lindenmoor 14, USA<br>
      Tel: +40 700 318 245<br>
      Fax: +40 700 642 190<br>
      www.harlowcrest.com
    </div>
    <div class="ring"></div>
  </div>

  <div class="piece letterhead">
    <div class="wordmark"><span class="dot"></span><span class="name">Harlow Crest</span></div>
    <div class="contact">
      <h4>CONTACT</h4>
      Str. Lindenmoor 14, USA<br>
      Tel: +40 700 318 245<br>
      Fax: +40 700 642 190
      <div class="web">www.harlowcrest.com</div>
    </div>
    <div class="letter">
      <div class="meta">TO: Clara Benton<br>Subject: Order status<br>Date: 30.01.2012</div>
      <p>Dear Ms. Clara Benton,<br>Thank you for your recent order. We are pleased to confirm that all items have been reviewed and scheduled for delivery this month. Our team will keep you informed of every step.</p>
      <p>Please review the attached summary and let us know if any details need to be adjusted before final approval is given.</p>
      <p>Should you have further questions about timing, financing or site preparation, our office is available on weekdays and will respond promptly to every request.</p>
      <p>We appreciate your continued trust and look forward to a long and productive partnership in the months ahead.</p>
      <div class="sign">Best regards,<br>Adrian Voss</div>
    </div>
    <div class="ring"></div>
  </div>

  <div class="section-label" style="left:97px; top:597px;">Presentation Cover</div>

  <div class="piece cover cover-front">
    <div class="wordmark"><span class="dot"></span><span class="name">Harlow Crest</span></div>
    <div class="edge"></div>
  </div>

  <div class="piece cover cover-back">
    <div class="ring"></div>
    <div class="contact">
      <div>Str. Lindenmoor 14, USA</div>
      <div class="phones">Tel: +40 700 318 245<br>Fax: +40 700 642 190</div>
      <div class="web">www.harlowcrest.com</div>
    </div>
  </div>

</body>
</html>
```